Website R86 coffee

I am opening a small business selling locally roasted coffee online. To start with I want a site with three pages. 1. A welcome page with logo and mission/vision. 2. Shopping/ordering page. 3. About Us page. The brand is "R86 Coffee - A warm start to every day". We are giving back to the downs syndrome community by employing people with down syndrome (Trisomy 21) and buy donating to down syndrome research.

Target Market(s)

Families and friends of people with downs syndrome

Coding

Coded - Design and coding required

Number of Pages Required

3 page

```html
<!DOCTYPE html>
<html lang="en">
<head>
<meta charset="utf-8">
<title>R86 Coffee – Home page concepts</title>
<link href="https://fonts.googleapis.com/css2?family=Montserrat:wght@300;400;500;600&display=swap" rel="stylesheet">
<style>
  :root{
    --stage:#e1e1e1;
    --ink:#222222;
    --text:#5a5a5a;
    --white:#ffffff;
    --blush:#f8ece8;
    --footer:#232323;
    --footer-line:#4a4a4a;
    --footer-text:#d8d8d8;
    --roast-dark:#2a1712;
    --roast-mid:#5a3322;
    --roast-warm:#8a5334;
    --kraft:#d9a166;
  }
  *{box-sizing:border-box;margin:0;padding:0}
  html,body{width:1200px;height:1158px;overflow:hidden}
  body{background:var(--stage);font-family:'Montserrat',sans-serif;color:var(--ink);position:relative}

  .page{position:absolute;top:105px;width:720px;height:1548px;transform:scale(.6122);transform-origin:0 0;
        background:var(--white);box-shadow:0 18px 40px rgba(0,0,0,.18);overflow:hidden}
  .page--classic{left:102px}
  .page--product{left:657px}

  /* hero */
  .hero{position:absolute;left:0;top:0;width:720px;height:429px}
  .page--classic .hero{background:radial-gradient(ellipse at 70% 30%,#7a5140 0%,var(--roast-mid) 35%,var(--roast-dark) 80%),var(--roast-dark)}
  .page--product .hero{background:linear-gradient(90deg,#3a2419 0%,var(--roast-dark) 35%,#4a2c1d 60%,var(--roast-warm) 85%,var(--kraft) 100%)}
  .hero__photo{position:absolute;inset:0}
  .page--classic .hero__photo{background:linear-gradient(180deg,rgba(0,0,0,.25) 0%,rgba(0,0,0,0) 40%,rgba(80,40,70,.35) 100%)}
  .page--product .hero__photo{background:linear-gradient(180deg,rgba(0,0,0,.15) 0%,rgba(0,0,0,0) 50%,rgba(30,15,10,.45) 100%)}
  .brand{position:absolute;left:66px;top:52px;color:var(--white);font-weight:300;font-size:26px;letter-spacing:2px}
  .nav{position:absolute;left:382px;top:44px;display:flex;gap:24px;color:var(--white);font-size:11px;font-weight:500}
  .nav a{color:inherit;text-decoration:none}
  .nav .is-current{text-decoration:underline;text-underline-offset:3px}
  .cart{position:absolute;left:621px;top:36px;width:33px;height:33px;border:1.5px solid var(--white);border-radius:50%;display:flex;align-items:center;justify-content:center}
  .hero__title{position:absolute;left:0;right:0;text-align:center;color:var(--white);font-weight:600}
  .page--classic .hero__title{top:200px;font-size:33px}
  .page--product .hero__title{top:155px;line-height:1.1}
  .hero__title .small{display:block;font-size:23px;font-weight:500}
  .hero__title .large{display:block;font-size:35px;margin-top:4px}
  .btn{position:absolute;display:flex;align-items:center;justify-content:center;border-radius:20px;font-size:12px;font-weight:500}
  .btn--light{background:var(--white);color:var(--ink);width:112px;height:36px;left:304px}
  .page--classic .btn--light{top:258px}
  .page--product .btn--light{top:243px}
  .dots{position:absolute;top:378px;left:321px;display:flex;gap:3px}
  .dots span{width:24px;height:3px;background:rgba(255,255,255,.4);border-radius:2px}
  .dots span:first-child{background:var(--white)}

  /* vision */
  .about{position:absolute;left:0;top:429px;width:720px;height:428px}
  .about h2{position:absolute;left:66px;font-size:26px;font-weight:600;letter-spacing:.5px}
  .about p{position:absolute;left:66px;font-size:10.5px;line-height:16px;color:var(--text)}
  .about .vision-h{top:48px}
  .about .vision-p{top:91px}
  .about .mission-h{top:164px}
  .about .mission-p{top:207px}
  .team-photo{position:absolute;left:370px;top:41px;width:284px;height:305px;border-radius:6px;
              background:linear-gradient(160deg,#8c8880 0%,#5b564f 45%,#6b4a35 75%,#c48a52 100%)}

  /* product band */
  .feature{position:absolute;left:0;top:857px;width:720px;height:360px;background:var(--blush)}
  .bags-photo{position:absolute;left:0;top:14px;width:360px;height:346px;
              background:radial-gradient(ellipse at 45% 40%,var(--kraft) 0%,#c88f5a 38%,rgba(120,70,40,.5) 70%,rgba(248,236,232,0) 100%)}
  .feature h2{position:absolute;left:425px;top:100px;font-size:25px;font-weight:600}
  .feature h3{position:absolute;left:425px;top:138px;font-size:17px;font-weight:500}
  .feature p{position:absolute;left:425px;top:180px;font-size:11px;line-height:17px;color:var(--text)}
  .btn--dark{background:var(--ink);color:var(--white);width:113px;height:37px;left:425px;top:237px}

  /* footer */
  .footer{position:absolute;left:0;top:1217px;width:720px;height:331px;background:var(--footer);color:var(--white)}
  .newsletter{position:absolute;left:73px;top:42px;font-size:16px;font-weight:600;line-height:21px}
  .signup{position:absolute;left:256px;top:40px;width:397px;height:38px;display:flex}
  .signup__field{flex:1;border:1px solid #8a8a8a;display:flex;align-items:center;padding-left:12px;font-size:10px;color:var(--white)}
  .signup__go{width:42px;background:var(--white);display:flex;align-items:center;justify-content:center}
  .footer__brand{position:absolute;left:67px;top:186px;width:131px;text-align:center;font-size:22px;font-weight:300;letter-spacing:2px}
  .footer__col{position:absolute;top:128px}
  .footer__col h4{font-size:9.5px;font-weight:600;margin-bottom:10px;letter-spacing:.3px}
  .footer__col li{list-style:none;font-size:10px;color:var(--footer-text);line-height:17px}
  .links{left:289px}
  .contact{left:466px}
  .contact li{display:flex;gap:7px;align-items:flex-start;margin-bottom:9px;line-height:14px}
  .contact svg{flex:none;margin-top:2px}
  .footer__rule{position:absolute;left:66px;top:274px;width:587px;height:1px;background:var(--footer-line)}
  .copyright{position:absolute;left:66px;top:293px;font-size:10px;color:var(--footer-text)}
  .social{position:absolute;left:567px;top:287px;display:flex;gap:5px}
  .social span{width:25px;height:25px;border:1px solid #9a9a9a;border-radius:50%}
</style>
</head>
<body>

<!-- Concept A -->
<section class="page page--classic">
  <header class="hero">
    <div class="hero__photo" role="img" aria-label="Photo of roasted coffee beans tumbling in a roaster drum"></div>
    <div class="brand">R86 COFFEE</div>
    <nav class="nav"><a class="is-current">HOME</a><a>ABOUT US</a><a>CONTACT US</a></nav>
    <div class="cart"><svg width="13" height="12" viewBox="0 0 13 12"><path d="M1 1h2l1.6 6.5h6L12 3H4" fill="none" stroke="#fff" stroke-width="1.4"/><circle cx="5" cy="10" r="1" fill="#fff"/><circle cx="10" cy="10" r="1" fill="#fff"/></svg></div>
    <h1 class="hero__title">A WARM START TO EVERY DAY</h1>
    <div class="btn btn--light">ORDER NOW!</div>
    <div class="dots"><span></span><span></span><span></span></div>
  </header>

  <section class="about">
    <h2 class="vision-h">VISION</h2>
    <p class="vision-p">Develop a company that markets coffee and<br>related products to family and friends of the down<br>syndrome community</p>
    <h2 class="mission-h">MISSION</h2>
    <p class="mission-p">Create and grow an online company selling<br>contract roasted coffee. as growth permits become<br>a fully vertically integrated coffee company from<br>roasting to our own coffee shop. The company will<br>give significant funds to medical research in<br>downs syndrome and we will hire as many people<br>with Downs syndrome as possible.</p>
    <div class="team-photo" role="img" aria-label="Photo of the café team in aprons beside an espresso machine"></div>
  </section>

  <section class="feature">
    <div class="bags-photo" role="img" aria-label="Photo of two kraft coffee bags with scattered coffee beans"></div>
    <h2>R86 COFFEE</h2>
    <h3>A warm start to every day</h3>
    <p>Premium Specialty coffee, delivered<br>straight to your door.</p>
    <div class="btn btn--dark">ORDER NOW!</div>
  </section>

  <footer class="footer">
    <div class="newsletter">NEWSLETTER<br>SUBSCRIPTION</div>
    <div class="signup"><div class="signup__field">EMAIL ADDRESS</div><div class="signup__go"><svg width="20" height="10" viewBox="0 0 20 10"><path d="M0 5h17M13 1l4 4-4 4" fill="none" stroke="#222" stroke-width="2"/></svg></div></div>
    <div class="footer__brand">R86 COFFEE</div>
    <div class="footer__col links"><h4>QUICK LINKS</h4><ul><li>Home</li><li>About us</li><li>Products</li><li>Contact</li><li>Terms and Conditions</li></ul></div>
    <div class="footer__col contact"><h4>CONTACT US</h4><ul>
      <li><svg width="7" height="10" viewBox="0 0 7 10"><path d="M3.5 10S0 5.5 0 3.5a3.5 3.5 0 0 1 7 0C7 5.5 3.5 10 3.5 10z" fill="#fff"/><circle cx="3.5" cy="3.5" r="1.3" fill="#232323"/></svg><span>24 Harlow Lane<br>Northcote Park, Victoria 3070</span></li>
      <li><svg width="9" height="9" viewBox="0 0 9 9"><path d="M1 .5l2 .2.7 2-1 .8a5 5 0 0 0 2.8 2.8l.8-1 2 .7.2 2C6 8.5.5 3 1 .5z" fill="#fff"/></svg><span>1 800 555 0186</span></li>
      <li><svg width="10" height="8" viewBox="0 0 10 8"><rect width="10" height="8" fill="#fff"/><path d="M0 0l5 4 5-4" fill="none" stroke="#232323" stroke-width="1"/></svg><span>hello@r86coffee.com</span></li>
    </ul></div>
    <div class="footer__rule"></div>
    <div class="copyright">© 2021 R86 coffee. All Rights Reserved.</div>
    <div class="social"><span></span><span></span><span></span></div>
  </footer>
</section>

<!-- Concept B -->
<section class="page page--product">
  <header class="hero">
    <div class="hero__photo" role="img" aria-label="Photo of a coffee scoop of beans on burlap, a steaming cup and a kraft coffee bag"></div>
    <div class="brand">R86 COFFEE</div>
    <nav class="nav"><a class="is-current">HOME</a><a>ABOUT US</a><a>CONTACT US</a></nav>
    <div class="cart"><svg width="13" height="12" viewBox="0 0 13 12"><path d="M1 1h2l1.6 6.5h6L12 3H4" fill="none" stroke="#fff" stroke-width="1.4"/><circle cx="5" cy="10" r="1" fill="#fff"/><circle cx="10" cy="10" r="1" fill="#fff"/></svg></div>
    <h1 class="hero__title"><span class="small">A WARM START</span><span class="large">TO EVERY DAY</span></h1>
    <div class="btn btn--light">ORDER NOW!</div>
    <div class="dots"><span></span><span></span><span></span></div>
  </header>

  <section class="about">
    <h2 class="vision-h">VISION</h2>
    <p class="vision-p">Develop a company that markets coffee and<br>related products to family and friends of the down<br>syndrome community</p>
    <h2 class="mission-h">MISSION</h2>
    <p class="mission-p">Create and grow an online company selling<br>contract roasted coffee. as growth permits become<br>a fully vertically integrated coffee company from<br>roasting to our own coffee shop. The company will<br>give significant funds to medical research in<br>downs syndrome and we will hire as many people<br>with Downs syndrome as possible.</p>
    <div class="team-photo" role="img" aria-label="Photo of the café team in aprons beside an espresso machine"></div>
  </section>

  <section class="feature">
    <div class="bags-photo" role="img" aria-label="Photo of two kraft coffee bags with scattered coffee beans"></div>
    <h2>R86 COFFEE</h2>
    <h3>A warm start to every day</h3>
    <p>Premium Specialty coffee, delivered<br>straight to your door.</p>
    <div class="btn btn--dark">ORDER NOW!</div>
  </section>

  <footer class="footer">
    <div class="newsletter">NEWSLETTER<br>SUBSCRIPTION</div>
    <div class="signup"><div class="signup__field">EMAIL ADDRESS</div><div class="signup__go"><svg width="20" height="10" viewBox="0 0 20 10"><path d="M0 5h17M13 1l4 4-4 4" fill="none" stroke="#222" stroke-width="2"/></svg></div></div>
    <div class="footer__brand">R86 COFFEE</div>
    <div class="footer__col links"><h4>QUICK LINKS</h4><ul><li>Home</li><li>About us</li><li>Products</li><li>Contact</li><li>Terms and Conditions</li></ul></div>
    <div class="footer__col contact"><h4>CONTACT US</h4><ul>
      <li><svg width="7" height="10" viewBox="0 0 7 10"><path d="M3.5 10S0 5.5 0 3.5a3.5 3.5 0 0 1 7 0C7 5.5 3.5 10 3.5 10z" fill="#fff"/><circle cx="3.5" cy="3.5" r="1.3" fill="#232323"/></svg><span>24 Harlow Lane<br>Northcote Park, Victoria 3070</span></li>
      <li><svg width="9" height="9" viewBox="0 0 9 9"><path d="M1 .5l2 .2.7 2-1 .8a5 5 0 0 0 2.8 2.8l.8-1 2 .7.2 2C6 8.5.5 3 1 .5z" fill="#fff"/></svg><span>1 800 555 0186</span></li>
      <li><svg width="10" height="8" viewBox="0 0 10 8"><rect width="10" height="8" fill="#fff"/><path d="M0 0l5 4 5-4" fill="none" stroke="#232323" stroke-width="1"/></svg><span>hello@r86coffee.com</span></li>
    </ul></div>
    <div class="footer__rule"></div>
    <div class="copyright">© 2021 R86 coffee. All Rights Reserved.</div>
    <div class="social"><span></span><span></span><span></span></div>
  </footer>
</section>

</body>
</html>
```